KT-Systems advertising flag and billboard design

I need a design for advertising flag and a design for billboard.
Information can be obtained from https://kt-sytronik.de.
Updates
Target Market(s)
IT service for companies
Requirements
Must have
- Logo, contact information and services

```html
<!DOCTYPE html>
<html lang="de">
<head>
<meta charset="utf-8">
<title>KT-Systems – Fahne und Plakatwand</title>
<link rel="stylesheet" href="https://fonts.googleapis.com/css2?family=Exo+2:ital,wght@0,400;0,500;0,600;0,700;0,800;0,900;1,800&display=swap">
<style>
  :root {
    --stage-light: #d9d9d9;
    --stage-dark: #9c9c9c;
    --flag-bg: #262626;
    --flag-text: #c9c9cc;
    --ink: #141414;
    --brand-blue: #1a0fd6;
    --brand-blue-deep: #0d06a8;
    --brand-blue-light: #4d7cf0;
    --label: #1f1f2e;
    --bar-grey-1: #f4f4f4;
    --bar-grey-2: #cfcfcf;
    --white: #ffffff;
  }
  * { box-sizing: border-box; margin: 0; padding: 0; }
  html, body { width: 887px; height: 1200px; overflow: hidden; }
  body {
    position: relative;
    font-family: "Exo 2", sans-serif;
    background: radial-gradient(ellipse at 50% 45%, var(--stage-light) 0%, var(--stage-dark) 100%);
  }

  /* Flag */
  .flag {
    position: absolute;
    left: 82px; top: 365px;
    width: 80px; height: 470px;
    background: var(--flag-bg);
    box-shadow: 0 10px 24px rgba(0,0,0,.35);
  }
  .flag-name {
    position: absolute;
    left: 50%; top: 50%;
    transform: translate(-50%, -50%) rotate(-90deg);
    white-space: nowrap;
    font-weight: 800;
    font-size: 44px;
    letter-spacing: 4px;
    text-transform: uppercase;
    color: var(--flag-text);
  }

  /* Billboard */
  .billboard {
    position: absolute;
    left: 208px; top: 430px;
    width: 600px; height: 300px;
    background: var(--white);
    overflow: hidden;
    box-shadow: 0 18px 30px rgba(0,0,0,.3);
  }
  .billboard-photo {
    position: absolute; inset: 0;
    clip-path: polygon(0 0, 330px 0, 222px 248px, 0 248px);
    background: linear-gradient(100deg, #9d1010 0%, #c84a4a 30%, #6a9ed8 60%, #2aa3e8 100%);
  }
  .billboard-stripe {
    position: absolute; inset: 0;
    clip-path: polygon(330px 0, 337px 0, 230px 248px, 222px 248px);
    background: var(--white);
  }
  .billboard-blue-slash {
    position: absolute; inset: 0;
    clip-path: polygon(300px 70px, 318px 40px, 230px 248px, 212px 248px);
    background: var(--brand-blue);
  }

  .brand-name {
    position: absolute;
    right: 30px; top: 22px;
    font-weight: 800;
    font-size: 24px;
    letter-spacing: 2px;
    text-transform: uppercase;
    color: var(--brand-blue);
  }
  .headline {
    position: absolute;
    right: 30px; top: 58px;
    text-align: right;
    font-weight: 600;
    font-size: 44px;
    line-height: 44px;
    color: var(--ink);
  }
  .headline em {
    font-style: italic;
    font-weight: 800;
    color: var(--brand-blue);
  }

  .services {
    position: absolute;
    left: 290px; top: 158px;
    width: 290px;
    display: flex;
    justify-content: space-between;
    list-style: none;
  }
  .service {
    width: 72px;
    display: flex; flex-direction: column; align-items: center;
    font-weight: 500;
    font-size: 11.5px;
    line-height: 13px;
    color: var(--label);
    text-align: center;
  }
  .service-icon {
    width: 40px; height: 40px;
    margin-bottom: 6px;
  }

  .support-bar {
    position: absolute;
    left: 0; bottom: 0;
    width: 100%; height: 52px;
    background: linear-gradient(90deg, var(--bar-grey-1), var(--bar-grey-2) 40%);
  }
  .support-question {
    position: absolute;
    left: 20px; top: 8px;
    font-weight: 700;
    font-size: 14.5px;
    line-height: 17px;
    text-transform: uppercase;
    color: var(--ink);
  }
  .phone-band {
    position: absolute;
    right: 0; top: 0;
    width: 375px; height: 52px;
    clip-path: polygon(0 0, 100% 0, 100% 100%, 12px 100%);
    background: linear-gradient(90deg, var(--brand-blue-deep) 0%, var(--brand-blue) 60%, var(--brand-blue-light) 100%);
  }
  .phone-number {
    position: absolute;
    right: 24px; top: 4px;
    font-weight: 800;
    font-size: 38px;
    letter-spacing: 1px;
    color: var(--white);
  }
  .phone-icon {
    position: absolute;
    left: 213px; top: 5px;
    width: 42px; height: 42px;
  }
</style>
</head>
<body>

  <section class="flag" aria-label="Werbefahne">
    <span class="flag-name">KT-Systems</span>
  </section>

  <section class="billboard" aria-label="Plakatwand">
    <div class="billboard-photo" role="img" aria-label="Foto: Hand berührt eine leuchtende digitale Netzwerkoberfläche"></div>
    <div class="billboard-stripe"></div>
    <div class="billboard-blue-slash"></div>

    <div class="brand-name">KT-Systems</div>

    <h1 class="headline">Ihr Partner<br>für <em>IT-Service</em></h1>

    <ul class="services">
      <li class="service">
        <svg class="service-icon" viewBox="0 0 40 40" aria-hidden="true">
          <circle cx="20" cy="20" r="19" fill="#1a0fd6" stroke="#b9c6ff" stroke-width="2"/>
          <path d="M20 10a6 6 0 0 0-6 6c0 5 6 11 6 11s6-6 6-11a6 6 0 0 0-6-6z" fill="none" stroke="#fff" stroke-width="1.6"/>
          <circle cx="20" cy="16" r="2.2" fill="none" stroke="#fff" stroke-width="1.4"/>
          <ellipse cx="20" cy="28" rx="8" ry="2.2" fill="none" stroke="#fff" stroke-width="1.2"/>
        </svg>
        An jeden Ort
      </li>
      <li class="service">
        <svg class="service-icon" viewBox="0 0 40 40" aria-hidden="true">
          <circle cx="20" cy="20" r="19" fill="#1a0fd6" stroke="#b9c6ff" stroke-width="2"/>
          <path d="M12 12l16 16M28 12L12 28" stroke="#fff" stroke-width="2" stroke-linecap="round"/>
          <circle cx="12.5" cy="12.5" r="2.5" fill="none" stroke="#fff" stroke-width="1.4"/>
          <circle cx="27.5" cy="27.5" r="2.5" fill="none" stroke="#fff" stroke-width="1.4"/>
        </svg>
        Remote Service
      </li>
      <li class="service">
        <svg class="service-icon" viewBox="0 0 40 40" aria-hidden="true">
          <circle cx="20" cy="20" r="19" fill="#1a0fd6" stroke="#b9c6ff" stroke-width="2"/>
          <circle cx="20" cy="17" r="7" fill="none" stroke="#fff" stroke-width="1.6"/>
          <path d="M16 23l-2 7 4-2 2 3M24 23l2 7-4-2-2 3" fill="none" stroke="#fff" stroke-width="1.4"/>
          <path d="M20 13.5l1.1 2.3 2.4.3-1.8 1.7.5 2.4-2.2-1.2-2.2 1.2.5-2.4-1.8-1.7 2.4-.3z" fill="#fff"/>
        </svg>
        Nur geprüfte Hersteller
      </li>
      <li class="service">
        <svg class="service-icon" viewBox="0 0 40 40" aria-hidden="true">
          <circle cx="20" cy="20" r="19" fill="#1a0fd6" stroke="#b9c6ff" stroke-width="2"/>
          <rect x="11" y="12" width="16" height="15" rx="2" fill="none" stroke="#fff" stroke-width="1.6"/>
          <path d="M11 16h16M15 10v4M23 10v4" stroke="#fff" stroke-width="1.6"/>
          <circle cx="27" cy="26" r="4.5" fill="#1a0fd6" stroke="#fff" stroke-width="1.4"/>
          <path d="M27 24v2.2h1.8" stroke="#fff" stroke-width="1.2" fill="none"/>
        </svg>
        7 Tage pro Woche
      </li>
    </ul>

    <div class="support-bar">
      <p class="support-question">Benötigen Sie<br>technischen Support?</p>
      <div class="phone-band">
        <span class="phone-number">01234-5557890</span>
      </div>
      <svg class="phone-icon" viewBox="0 0 42 42" aria-hidden="true">
        <circle cx="21" cy="21" r="19" fill="#141414" stroke="#fff" stroke-width="2"/>
        <path d="M15 13c-1.5 1.5-1.5 4 1 8s5.5 7 8.5 8c2 .6 3.5-.5 4.5-1.5l-3-3-2 1.5c-2-1-4.5-3.5-5.5-5.5l1.5-2-3-3.5z" fill="#fff"/>
        <path d="M23 12a7 7 0 0 1 7 7M23 15.5a3.5 3.5 0 0 1 3.5 3.5" stroke="#fff" stroke-width="1.4" fill="none"/>
      </svg>
    </div>
  </section>

</body>
</html>
```